Flyer-Design für ambulanten Pflegedienst
Zielgruppe
Wir sind ein ambulanter Pflegedienst in Rostock und in Gnoien. Patienten werden in der Häuslichkeit versorgt.
Aufgabenstellung
Folgender Flyer soll erstellt werden.
Das Format kann vom Designer festgelegt werden:
Ein paar Flyer habe ich mit hochgeladen. Es sollte jedoch einmal ein ganz neues modernes Design sein.
Vorderseite:Text:
Sie kommen mit den alltäglichen Dingen des Lebens
nicht mehr gut alleine zurecht?
Wir unterstützen Sie gerne bei der Beantragung eines
Pflegegrades. Nachdem der Ärztliche Prüfstelle der Versicherer
sich angemeldet hat, begleiten wir Sie bei der Begutachtung.
Rückseite:
Pflegeberatung:
Wenn Sie einen Pflegegrad haben und von einer privaten Pflegeperson
versorgt werden, erwartet Ihre Pflegekasse in regelmäßigen Abständen einen Beratungebesuch
von einem anerkannten Pflegedienst.
Bitte beide Logos vom Pflegehaus Lindental und vom Pflegedienst Kavuro auf den Flyer
Auch beide Adressen auf den Flyer:

```html
<!DOCTYPE html>
<html lang="de">
<head>
<meta charset="utf-8">
<title>Flyer Pflegedienst Kavuro</title>
<link href="https://fonts.googleapis.com/css2?family=Dosis:wght@500;600;700&family=Montserrat:wght@400;500;600&display=swap" rel="stylesheet">
<style>
  :root{
    --green:#7cc242;
    --white:#ffffff;
    --paper:#fbfbf7;
    --ink:#262626;
    --text:#3a3a3a;
    --stage:#e9e9e6;
    --photo-warm:#d9d2c8;
    --photo-cool:#c8d3dc;
  }
  *{margin:0;padding:0;box-sizing:border-box}
  html,body{width:1200px;height:902px;overflow:hidden;background:var(--stage)}
  .canvas{position:relative;width:1200px;height:902px}
  .flyer{position:absolute;top:55px;width:560px;height:792px;background:var(--paper);overflow:hidden;box-shadow:0 4px 18px rgba(0,0,0,.12)}
  .flyer--back{left:25px}
  .flyer--front{left:615px}
  .shape{position:absolute;left:0;top:0}
  .photo{position:absolute;left:0;width:560px}
  .photo--back{top:0;height:330px;background:linear-gradient(120deg,var(--photo-warm) 0%,#eeeae4 55%,#f6f6f4 100%)}
  .photo--front{top:500px;height:292px;background:linear-gradient(100deg,#3d7fc4 0%,#c9b59b 45%,var(--photo-cool) 100%)}
  .heading{font-family:'Dosis',sans-serif;font-weight:600;color:var(--ink)}
  .body{font-family:'Montserrat',sans-serif;font-size:13px;line-height:1.38;color:var(--text)}
  .brand{font-family:'Montserrat',sans-serif;font-weight:600;color:var(--green);text-align:center;font-size:13px;line-height:1.2}
  .brand-dot{display:block;width:34px;height:34px;border-radius:50%;background:var(--green);margin:0 auto 6px}

  /* back side */
  .advice{position:absolute;left:60px;top:365px;width:440px}
  .advice h2{font-size:19px;margin-bottom:12px}
  .advice p{margin-bottom:20px}
  .contact{position:absolute;left:0;top:612px;width:560px;text-align:center;color:var(--white);font-family:'Montserrat',sans-serif}
  .contact h2{font-family:'Dosis',sans-serif;font-weight:700;font-size:32px;margin-bottom:8px}
  .contact .org{font-weight:600;font-size:13px}
  .contact .line{font-size:12.5px;line-height:1.35}
  .contact .block{margin-bottom:8px}
  .corner{position:absolute;width:120px}
  .corner--left{left:10px;top:708px}
  .corner--right{right:8px;top:730px}

  /* front side */
  .top-brand{position:absolute;left:200px;top:26px;width:160px}
  .claim{position:absolute;left:0;top:130px;width:560px;text-align:center;font-family:'Dosis',sans-serif;font-weight:700;font-size:36px;line-height:1.15;color:var(--white);letter-spacing:.5px}
  .intro{position:absolute;left:62px;top:268px;width:440px}
  .intro h1{font-size:20px;line-height:1.25;margin-bottom:14px}
  .intro p{text-align:justify;margin-bottom:16px}
  .phone{display:flex;align-items:center;gap:8px;font-family:'Dosis',sans-serif;font-weight:700;font-size:20px;color:var(--ink);margin-top:-8px}
  .side-brand{position:absolute;right:44px;top:450px;font-size:12px}
</style>
</head>
<body>
<main class="canvas">

  <section class="flyer flyer--back">
    <div class="photo photo--back" role="img" aria-label="Foto: Pflegerin hilft einer lächelnden Seniorin beim Zuknöpfen der Bluse im Wohnzimmer"></div>

    <div class="advice">
      <h2 class="heading">Pflegeberatung</h2>
      <p class="body">Wenn Sie einen Pflegegrad haben und von einer privaten Pflegeperson versorgt werden, erwartet Ihre Pflegekasse in regelmäßigen Abständen einen Beratungebesuch von einem anerkannten Pflegedienst.</p>
      <p class="body">Vereinbaren Sie unter der Telefonnummer <strong>0800 5550142</strong> rechtzeitig einen Termin, damit ihre optimale Versorgung weiterhin sichergestellt ist.</p>
    </div>

    <svg class="shape" width="560" height="792" viewBox="0 0 560 792" aria-hidden="true">
      <path d="M0 720 C60 640 170 590 280 590 C390 590 500 640 560 720 L560 792 L0 792 Z" fill="var(--green)"/>
      <circle cx="55" cy="790" r="95" fill="var(--paper)"/>
      <circle cx="520" cy="790" r="100" fill="var(--paper)"/>
    </svg>

    <div class="contact">
      <h2>Kontakt</h2>
      <div class="block">
        <div class="org">Pflegehaus Lindental GmbH</div>
        <div class="line">Kastanienstraße 12 | 18990 Lindenfeld</div>
        <div class="line">www.Pflegehaus-Lindental.de</div>
      </div>
      <div class="block">
        <div class="org">Kavuro<br>Der mobile Pflegedienst GmbH</div>
        <div class="line">Am Mühlenteich 4 | 17990 Auenbrück</div>
        <div class="line">www.Kavuro.de</div>
      </div>
    </div>

    <div class="brand corner corner--left"><span class="brand-dot"></span>Pflegehaus Lindental</div>
    <div class="brand corner corner--right">Kavuro</div>
  </section>

  <section class="flyer flyer--front">
    <svg class="shape" width="560" height="792" viewBox="0 0 560 792" aria-hidden="true">
      <path d="M0 0 L560 0 L560 95 C520 190 410 240 280 240 C150 240 40 190 0 95 Z" fill="var(--green)"/>
      <ellipse cx="280" cy="20" rx="95" ry="95" fill="var(--paper)"/>
    </svg>

    <div class="brand top-brand"><span class="brand-dot"></span>Pflegehaus Lindental</div>

    <div class="claim">WIR KÜMMERN<br>UNS UM SIE!</div>

    <div class="intro">
      <h1 class="heading">Sie kommen mit den alltäglichen Dingen des Lebens nicht mehr gut alleine zurecht?</h1>
      <p class="body">Wir unterstützen Sie gerne bei der Beantragung eines Pflegegrades. Nachdem die Ärztliche Prüfstelle der Versicherer sich angemeldet hat, begleiten wir Sie bei der Begutachtung.</p>
      <p class="body">Unsere freundlichen Mitarbeiter erreichen Sie telefonisch unter der Telefonnummer:</p>
      <div class="phone">
        <svg width="16" height="16" viewBox="0 0 24 24" aria-hidden="true"><path fill="var(--ink)" d="M6.6 10.8c1.4 2.8 3.8 5.1 6.6 6.6l2.2-2.2c.3-.3.7-.4 1-.2 1.1.4 2.3.6 3.6.6.6 0 1 .4 1 1V20c0 .6-.4 1-1 1C10.6 21 3 13.4 3 4c0-.6.4-1 1-1h3.5c.6 0 1 .4 1 1 0 1.3.2 2.5.6 3.6.1.3 0 .7-.2 1z"/></svg>
        0800 5550142
      </div>
    </div>

    <div class="brand side-brand">Kavuro</div>

    <div class="photo photo--front" role="img" aria-label="Foto: Pflegerin in blauer Kleidung lacht gemeinsam mit einer Seniorin im Sessel"></div>
  </section>

</main>
</body>
</html>
```